Epoxy Flooring Contractor business card

We need a business card to promote a new addition to our business. We now offer Epoxy Flooring. We would like for the business card to include the images attached. One is our logo, the other is a sample of metallic epoxy flooring, we would like to incorporate that somewhere into the design. I was thinking an icon of a man pushing a concrete grinder and have the color set to the metallic epoxy color. I found a business card sample on this website, I will attach it. It has the icon that we are looking for, or something similar.
Our company name is Harborline Coatings LLC
Our owners name is Dane Morrow
Phone is 561-482-7160
website is www.harborline-coatingsllc.example
please let me know if you need any other info

Contact Information for Business Card

Harborline Coatings LLC
Dane Morrow, owner
Phone: 561-482-7160
Address: P.O Box 8241 Lake Worth, FL 33467
www.Harborline-CoatingsLLC.example
HarborlineCoatingsLLC@mailbox.example
Include logo attached
It must include a Clip art of man with concrete grinder
Must include metallic epoxy design attached
Must include the following text
Residential Garage Flooring
Epoxy Countertops
Commercial Epoxy Flooring
Restaurant Flooring
Warehouse Flooring
Licensed & Insured
Free Estimates

Colors

Designer to choose colors to be used in the design.

Requirements
Must have
• Include logo attached
• It must include a Clip art of man with concrete grinder
• Must include metallic epoxy design attached
• Must include the following text
• Garage Epoxy Flooring
• Residential Epoxy Flooring
• Concrete Floor Crack Repairs
• Concrete Floor Grinding
• Commercial & Warehouse Epoxy Flooring
• Restaurant Epoxy Flooring
• Epoxy Countertops
• Non Slip Epoxy Pool Decks
• Textured Finishes, Flakes, Granite Coat, Metallic & Quartz
• FREE ESTIMATES • LICENSED & INSURED

```html
<!DOCTYPE html>
<html lang="en">
<head>
<meta charset="utf-8">
<title>Harborline Coatings LLC – Business Card</title>
<link rel="stylesheet" href="https://fonts.googleapis.com/css2?family=Roboto:ital,wght@0,400;0,500;1,400;1,500&display=swap">
<style>
  :root {
    --bg: #2e3034;
    --card-white: #ffffff;
    --brand-blue: #3f5f82;
    --brand-blue-soft: #4d6e93;
    --ink-blue: #2f4f74;
    --rule-blue: #7f98b8;
    --text-grey: #55585d;
    --on-blue: #ffffff;
    --epoxy-dark: #3d3a36;
    --epoxy-mid: #7a6f62;
    --epoxy-light: #b8aea0;
  }
  * { margin: 0; padding: 0; box-sizing: border-box; }
  html, body { width: 1200px; height: 900px; overflow: hidden; }
  body {
    background: var(--bg);
    font-family: "Roboto", Arial, sans-serif;
    position: relative;
  }
  .card {
    position: absolute;
    left: 250px;
    width: 700px;
    height: 400px;
    border-radius: 22px;
    overflow: hidden;
  }
  .card--front { top: 30px; background: var(--card-white); }
  .card--back { top: 470px; background: var(--brand-blue); }

  /* front */
  .name-marker {
    position: absolute; left: 0; top: 64px;
    width: 8px; height: 46px; background: var(--brand-blue);
  }
  .person-name {
    position: absolute; left: 40px; top: 58px;
    font-size: 40px; font-weight: 500; font-style: italic;
    color: var(--ink-blue); letter-spacing: -1px; text-transform: uppercase;
  }
  .person-role {
    position: absolute; left: 42px; top: 104px;
    font-size: 17px; font-style: italic; color: var(--text-grey);
  }
  .divider {
    position: absolute; left: 28px; right: 80px; top: 178px;
    height: 2px; background: var(--rule-blue);
  }
  .contact-list {
    position: absolute; left: 30px; top: 196px;
    list-style: none; font-size: 17px; font-style: italic; color: var(--text-grey);
    line-height: 29px;
  }
  .contact-list li { display: flex; align-items: center; gap: 10px; }
  .contact-list svg { width: 14px; height: 14px; flex: none; }
  .brand {
    position: absolute; display: flex; align-items: center; gap: 14px;
  }
  .brand__square { width: 44px; height: 44px; flex: none; }
  .brand__name {
    font-weight: 500; letter-spacing: 2px; line-height: 1.05;
  }
  .card--front .brand { right: 70px; top: 58px; }
  .card--front .brand__square { background: var(--brand-blue); }
  .card--front .brand__name { font-size: 30px; color: var(--ink-blue); }
  .address {
    position: absolute; right: 80px; bottom: 34px;
    font-size: 18px; font-style: italic; color: var(--text-grey);
    line-height: 26px; text-align: left;
  }
  .epoxy-strip {
    position: absolute; right: 0; top: 0; bottom: 0; width: 28px;
    background: linear-gradient(180deg, var(--epoxy-light), var(--epoxy-mid) 35%, var(--epoxy-dark) 60%, var(--epoxy-mid) 85%, var(--epoxy-light));
  }

  /* back */
  .grinder-artwork {
    position: absolute; left: 20px; top: -20px;
    width: 260px; height: 440px; border-radius: 120px 120px 40px 40px;
    background: radial-gradient(ellipse at 50% 40%, var(--brand-blue-soft), var(--brand-blue) 75%);
  }
  .card--back .brand { left: 230px; top: 70px; }
  .card--back .brand__square { background: var(--on-blue); width: 60px; height: 60px; }
  .card--back .brand__name { font-size: 42px; color: var(--on-blue); }
  .services {
    position: absolute; left: 130px; top: 230px; right: 30px;
    list-style: none; color: var(--on-blue);
    font-size: 19px; font-style: italic; line-height: 30px; letter-spacing: 0.5px;
  }
</style>
</head>
<body>

<section class="card card--front" aria-label="Business card front">
  <div class="name-marker"></div>
  <h1 class="person-name">Dane Morrow</h1>
  <p class="person-role">Owner</p>
  <div class="divider"></div>
  <ul class="contact-list">
    <li>
      <svg viewBox="0 0 16 16" aria-hidden="true"><path d="M4 1.5l2.2 3-1.4 1.6c.8 2 2.3 3.5 4.3 4.3l1.6-1.4 3 2.2-1 2.8C7.5 14 2 8.5 1.2 2.5z" fill="var(--brand-blue)"/></svg>
      561-482-7160
    </li>
    <li>
      <svg viewBox="0 0 16 16" aria-hidden="true"><rect x="1" y="3" width="14" height="10" rx="1" fill="none" stroke="var(--brand-blue)" stroke-width="1.6"/><path d="M1.5 4l6.5 5 6.5-5" fill="none" stroke="var(--brand-blue)" stroke-width="1.6"/></svg>
      HarborlineCoatingsLLC@mailbox.example
    </li>
    <li>
      <svg viewBox="0 0 16 16" aria-hidden="true"><circle cx="8" cy="8" r="6.5" fill="none" stroke="var(--brand-blue)" stroke-width="1.4"/><ellipse cx="8" cy="8" rx="3" ry="6.5" fill="none" stroke="var(--brand-blue)" stroke-width="1.2"/><path d="M1.5 8h13" stroke="var(--brand-blue)" stroke-width="1.2"/></svg>
      www.Harborline-CoatingsLLC.example
    </li>
  </ul>
  <div class="brand">
    <div class="brand__square"></div>
    <p class="brand__name">Harborline<br>Coatings</p>
  </div>
  <address class="address">P.O Box 8241 Lake<br>Worth, FL 33467</address>
  <div class="epoxy-strip" role="img" aria-label="Metallic epoxy floor sample texture"></div>
</section>

<section class="card card--back" aria-label="Business card back">
  <div class="grinder-artwork" role="img" aria-label="Faint clip art of a man pushing a concrete grinder"></div>
  <div class="brand">
    <div class="brand__square"></div>
    <p class="brand__name">Harborline<br>Coatings</p>
  </div>
  <ul class="services">
    <li>Residential Garage Flooring | Epoxy Countertops</li>
    <li>Commercial Epoxy Flooring | Restaurant Flooring</li>
    <li>Warehouse Flooring | Licensed &amp; Insured | Free Estimates</li>
  </ul>
</section>

</body>
</html>
```